Kestrel Ridge Equines flyer

Kestrel Ridge Equines is a boutique Morgan Horse Stud in Northern Tasmania.
Resident stallion: Bellhaven Starlight, 15hh black/brown.
Sire: Corlin's Evening Waltz
(IMP NZ dec)
Dam: Amber Gale Silhouette
(IMP USA. Carries the Dalmorren bloodline.)

We aim to produce beautiful, intelligent, well bred Morgans the whole family can enjoy, suitable for any discipline.

We have purebred and partbred stock for sale.

Must have
Double sided.
Web address,stud contact details.
Same font as logo.
tag line ' Selective breeding creates a masterpiece'

Would be nice to have stallions breeding as possible watermark

We need a new design, so we can distribute flyers/cards at equine events.

HI, Please review the brief, it has been update. Have also uploaded some extra photo's just in case. If you have a particular photo your chasing, let me know and i'll upload one if i have it. Cheers :)

Boutique

• Copperplate Gothic

Requirements
Must have
• Purebred & partbred stock for sale.

```html
<!DOCTYPE html>
<html lang="en">
<head>
<meta charset="utf-8">
<title>Kestrel Ridge Equines — Flyer</title>
<link href="https://fonts.googleapis.com/css2?family=Cinzel:wght@600;700&family=Open+Sans:wght@600;700&display=swap" rel="stylesheet">
<style>
  :root {
    --page-bg: #2b2b2d;
    --white: #ffffff;
    --teal: #1fa9bf;
    --teal-light: #33bcd0;
    --teal-dark: #138ea3;
    --pink: #c650b9;
    --pink-dark: #a93aa0;
    --purple: #9c3b9f;
    --photo-sky: #9fb8c9;
    --photo-field: #8d8a3a;
    --photo-horse: #4a2a18;
    --ribbon-shadow: rgba(0,0,0,0.25);
  }
  * { box-sizing: border-box; margin: 0; padding: 0; }
  html, body { width: 959px; height: 1200px; overflow: hidden; }
  body { background: var(--page-bg); position: relative; font-family: "Open Sans", Arial, sans-serif; }

  .flyer {
    position: absolute; left: 100px; top: 49px;
    width: 760px; height: 1102px;
    background: var(--white); overflow: hidden;
    box-shadow: 0 10px 30px rgba(0,0,0,0.5);
  }
  .hero-photo {
    position: absolute; left: 0; top: 0; width: 760px; height: 428px;
    background:
      radial-gradient(ellipse 260px 300px at 330px 250px, var(--photo-horse) 0%, rgba(74,42,24,0.85) 55%, rgba(74,42,24,0) 100%),
      linear-gradient(180deg, var(--photo-sky) 0%, #d8e2ea 30%, #5f7a3c 48%, var(--photo-field) 100%);
  }
  .hero-rail {
    position: absolute; left: 0; top: 416px; width: 760px; height: 12px;
    background: #8a6a44;
  }
  .content-band {
    position: absolute; left: 0; top: 440px; width: 760px; height: 491px;
    background: linear-gradient(90deg, var(--teal-dark) 0%, var(--teal-light) 50%, var(--teal-dark) 100%);
  }
  .footer-band {
    position: absolute; left: 0; top: 931px; width: 760px; height: 171px;
    border-top: 10px solid var(--white);
    background: linear-gradient(90deg, var(--pink-dark) 0%, var(--pink) 50%, var(--pink-dark) 100%);
  }
  .name-ribbon {
    position: absolute; left: 214px; top: 369px; width: 332px; height: 118px;
    filter: drop-shadow(0 3px 4px var(--ribbon-shadow));
  }
  .name-ribbon-label {
    position: absolute; left: 214px; top: 369px; width: 332px; height: 118px;
    display: flex; align-items: center; justify-content: center;
    font-family: "Cinzel", "Times New Roman", serif; font-weight: 700;
    font-size: 19px; color: var(--purple); letter-spacing: 0.5px;
  }
  .title-rule {
    position: absolute; height: 2px; background: var(--white);
  }
  .title-rule.top { left: 80px; top: 548px; width: 600px; }
  .title-rule.bottom { left: 80px; top: 644px; width: 600px; }
  .title {
    position: absolute; left: 0; top: 552px; width: 760px; text-align: center;
    font-family: "Cinzel", "Times New Roman", serif; font-weight: 700;
    font-size: 46px; line-height: 56px; color: var(--white); letter-spacing: 1px;
  }
  .tagline {
    position: absolute; left: 0; top: 604px; width: 760px; text-align: center;
    font-weight: 700; font-size: 27px; line-height: 36px; color: var(--white);
  }
  .intro {
    position: absolute; left: 60px; top: 676px; width: 640px; text-align: center;
    font-weight: 600; font-size: 17.5px; line-height: 25px; color: var(--white);
  }
  .stock-pill {
    position: absolute; left: 155px; top: 750px; width: 450px; height: 40px;
    border: 3px solid var(--white); border-radius: 20px;
    display: flex; align-items: center; justify-content: center;
    font-weight: 700; font-size: 17.5px; color: var(--white);
  }
  .gallery {
    position: absolute; left: 60px; top: 840px; width: 640px; height: 144px;
    background: var(--white); border-radius: 22px;
    box-shadow: 0 3px 8px rgba(0,0,0,0.25);
    display: flex; justify-content: space-between; align-items: center;
    padding: 0 20px;
  }
  .gallery-photo {
    width: 182px; height: 112px; border: 4px solid var(--purple); border-radius: 10px;
  }
  .gallery-photo.herd { background: linear-gradient(180deg, #6f8c5a 0%, #a98a60 55%, #b9a884 100%); }
  .gallery-photo.palomino { background: linear-gradient(180deg, #8aa56a 0%, #d8c995 50%, #c9b57a 100%); }
  .gallery-photo.rearing { background: linear-gradient(180deg, #9fb6c8 0%, #567a3f 45%, #7a3a20 75%, #6a8a40 100%); }
  .contact {
    position: absolute; left: 0; top: 1015px; width: 760px; text-align: center;
    font-weight: 600; font-size: 17.5px; line-height: 25px; color: var(--white);
  }
  .contact-line { display: flex; justify-content: center; align-items: center; gap: 8px; }
  .phone-icon { width: 18px; height: 18px; }
</style>
</head>
<body>
  <main class="flyer">
    <div class="hero-photo" role="img" aria-label="Photograph of a bay Morgan stallion standing behind a fence in a sunny paddock"></div>
    <div class="hero-rail"></div>
    <div class="content-band"></div>
    <div class="footer-band"></div>

    <svg class="name-ribbon" viewBox="0 0 332 118" aria-hidden="true">
      <polygon points="0,22 332,22 310,70 332,118 0,118 22,70" fill="#ffffff"/>
      <polygon points="24,0 308,0 308,22 24,22" fill="#ffffff"/>
      <polygon points="0,22 24,0 24,22" fill="#d9d9d9"/>
      <polygon points="332,22 308,0 308,22" fill="#d9d9d9"/>
    </svg>
    <div class="name-ribbon-label">Kestrel Ridge Equines</div>

    <div class="title-rule top"></div>
    <h1 class="title">Kestrel Ridge Equines</h1>
    <p class="tagline">Selective breeding creates a masterpiece</p>
    <div class="title-rule bottom"></div>

    <p class="intro">We aim to produce beautiful, intelligent, well bred Morgans the whole family can enjoy, suitable&nbsp; for any discipline.</p>
    <p class="stock-pill">We have purebred and partbred stock for sale.</p>

    <div class="gallery">
      <div class="gallery-photo herd" role="img" aria-label="Photograph of a small group of Morgan horses in a paddock"></div>
      <div class="gallery-photo palomino" role="img" aria-label="Photograph of a palomino Morgan standing in a grassy field"></div>
      <div class="gallery-photo rearing" role="img" aria-label="Photograph of a chestnut Morgan rearing in a paddock"></div>
    </div>

    <div class="contact">
      <p>Kestrel Ridge Equines PO Box 482 Lowmere TAS 7261</p>
      <p class="contact-line">
        <span>0400 123 987</span>
        <svg class="phone-icon" viewBox="0 0 18 18" aria-label="Phone">
          <rect x="0" y="0" width="18" height="18" rx="3" fill="#ffffff"/>
          <path d="M5 4 L7.5 4 L8.3 6.8 L7 8 C7.8 9.6 8.6 10.4 10 11 L11.2 9.7 L14 10.5 L14 13 C9 13.5 4.5 9 5 4 Z" fill="#b43ea9"/>
        </svg>
        <span>www.kestrelridgeequines.com</span>
      </p>
    </div>
  </main>
</body>
</html>
```